Flyer, poster, banner and social media titles designs for Community Renewal Guidlines

The Shared Guidelines for Community Renewal provide a nationally agreed framework to guide recovery policy and practice across Australia. The Principles support recovery practitioners, governments, non-government organisations and communities to deliver effective, community-centred recovery outcomes.
The Principles have recently been refreshed through extensive consultation and we require a contemporary visual identity and design suite that will increase awareness, engagement and practical application of the Principles.
The redesign will cover:
• A4 Brochure (primary publication)
• A3 Poster
• Pull up banner
• Social Media Tiles
The new design should:
• Create a recognisable brand for the Shared Guidelines.
• Appeal to both experienced and emerging recovery practitioners.
• Reflect contemporary disaster recovery practice.
• Feel people-focused rather than government-focused.
• Support future resources such as videos, implementation guides, presentations and workshop materials.
• Remain relevant for several years without requiring a major redesign.
Target Audience
• Disaster recovery practitioners
• Government agencies
• Non-government organisations
• Community recovery workers
• Recovery managers and leaders
• Community stakeholders and volunteers
The visual identity should reflect the six Principles:
• Understanding Context
• Recognising Complexity
• Community-Centred Approaches
• Coordination
• Communication
• Capacity Building
The design should communicate:
• Recovery is centred on people and communities.
• Recovery is collaborative and involves many sectors.
• Recovery is adaptive, inclusive and evidence-informed.
• Recovery supports resilience and long-term wellbeing.
• The Principles provide practical guidance for recovery practice.
We are looking for:
• Modern and professional
• Warm and approachable
• Human-centred
• Inclusive and accessible
• Australian in context
• Visually engaging
• Suitable for print and digital use
We would like to avoid:
• Images of disaster destruction
• Emergency response imagery (fire trucks, flashing lights, etc.)
• Overly corporate or bureaucratic designs
• Designs that focus on deficits rather than recovery and growth
Consider themes such as:
• Connection and collaboration
• Communities and people
• Growth, recovery and renewal
Accessibility
Designs should:
• Meet accessibility best practice
• Use clear typography
• Achieve strong colour contrast
• Be suitable for both digital and print formats

Deliverables
1. Principles Brochure
• A4 trifold size x 2 (online and print friendly version)
• A side to include cover side, logos side and overview of principles.
• B side full details of the principles
• Graphic to highlight the 3 c’s concept (RECOVERY Context, complexity, community centred, coordinate, communicate and capacity). Currently 3 circles.
• Can be printed and distributed electronically
2. Poster
• A1 and A3 versions
• Suitable for office and workshop display
3. Pull-Up Banner - 850 mm (W) × 2000 mm (H)
• Conference and event use
• High visual impact
• Strong branding and concise messaging
4. Social Media Tiles x 3
Updates

We are providing an extension and increasing the budget following feedback from designers. We are wanting the resources to look and feel different from the existing designs, considering either a different colour palette in the designs or different motif with the leave design. Any nature based designs should consider the Australian fauna or flora. Also suggest avoiding images in the designs. The principles are not numbered or liner in the concept of how they function. Happy to answer any further questions and thank you for your suggested concepts.

Target Market(s)

Disaster recovery practitioners, Government agencies , Non-government organisations, Community recovery workers and Community stakeholders and volunteers

Industry/Entity Type

Disaster recovery

Colors

Designer to choose colors to be used in the design.

Requirements
Must have
• Modern, warm, visually engaging, human-centred, Australian in context and different to the current design.
Nice to have
• Symbols for each principles
Should not have
• Images of disaster destruction, Emergency response imagery, Overly corporate or bureaucratic designs, Designs that focus on deficits rather than recovery and growth, avoid too much black

```html
<!DOCTYPE html>
<html lang="en">
<head>
<meta charset="utf-8">
<title>Shared Guidelines for Community Renewal – Design Suite</title>
<link href="https://fonts.googleapis.com/css2?family=Montserrat:wght@400;500;600;700&family=Source+Serif+4:wght@500;600&display=swap" rel="stylesheet">
<style>
:root{
  --navy:#0f2a3a;
  --forest:#1f4a2e;
  --lime:#7ba33a;
  --lime-soft:#a8c46a;
  --teal:#1d6a70;
  --blue:#1c5f8c;
  --cream:#f4f0e2;
  --sage:#e6e8d2;
  --ink:#1f2a2c;
  --muted:#4b5652;
  --white:#ffffff;
}
*{box-sizing:border-box;margin:0;padding:0}
html,body{width:1200px;height:800px;overflow:hidden;background:#ffffff}
body{position:relative;font-family:"Montserrat",sans-serif;color:var(--ink)}
.abs{position:absolute}
.icon-dot{border-radius:50%;display:flex;align-items:center;justify-content:center}
.icon-dot svg{width:62%;height:62%;stroke:#fff;fill:none;stroke-width:1.6;stroke-linecap:round;stroke-linejoin:round}

/* Brochure outside */
.panel{position:absolute;top:8px;height:502px;overflow:hidden}
.cover{left:9px;width:261px;background:var(--navy);color:#fff}
.eyebrow{font-weight:600;font-size:11px;letter-spacing:.4px;text-transform:uppercase}
.title-a{font-family:"Source Serif 4",serif;font-weight:600;line-height:.95;color:#fff}
.title-b{font-family:"Source Serif 4",serif;font-weight:600;line-height:.95;color:var(--lime)}
.hl{color:var(--lime-soft)}
.brand{display:flex;align-items:center;gap:7px}
.brand .mark{border-radius:50%;border:2px solid currentColor;flex:none}
.brand .name{font-weight:500;line-height:1.15}
.brand .sub{font-weight:600;letter-spacing:.8px}
.partners{left:270px;width:261px;background:var(--cream)}
.partner-grid{position:absolute;left:22px;right:16px;top:52px;display:grid;grid-template-columns:1fr 1fr;row-gap:30px;column-gap:10px}
.partner{display:flex;align-items:center;gap:6px;font-size:8.5px;font-weight:600;line-height:1.2;color:var(--navy)}
.partner .shape{width:22px;height:22px;border-radius:50%;background:#c9cdb8;flex:none}
.about{left:531px;width:252px;background:var(--cream)}
.h-teal{font-weight:700;font-size:11px;color:var(--teal);letter-spacing:.3px;text-transform:uppercase}
.body-s{font-size:7.4px;line-height:1.45;color:var(--ink)}

/* Poster */
.poster{position:absolute;left:816px;top:9px;width:373px;height:579px;background:var(--cream);overflow:hidden}
.poster-top{position:absolute;left:0;top:0;width:373px;height:150px;background:var(--navy)}
.pill{background:var(--lime);color:#fff;font-weight:600;font-size:11px;letter-spacing:.6px;border-radius:4px;padding:3px 9px}
.principle{position:absolute;left:27px;width:320px;display:flex;gap:12px}
.principle .icon-dot{width:40px;height:40px;flex:none}
.principle h3{font-family:"Source Serif 4",serif;font-weight:500;font-size:12px;color:var(--navy)}
.principle h3 b{font-family:"Montserrat",sans-serif;font-weight:600;color:var(--teal);font-size:11.5px}
.principle p{font-size:6.6px;line-height:1.4;color:var(--muted);margin-top:3px}

/* 3C */
.threec{position:absolute;left:9px;top:525px;width:495px;height:268px;background:var(--sage);overflow:hidden}
.enabler{position:absolute;left:306px;display:flex;gap:10px;width:180px}
.enabler .icon-dot{width:34px;height:34px;flex:none}
.enabler h4{font-size:9px;font-weight:600;color:var(--teal)}
.enabler p{font-size:7.4px;line-height:1.4;margin-top:3px}
.c-label{font-size:8px;font-weight:600}
.c-text{font-size:6.3px;line-height:1.4}

/* Banner */
.banner{position:absolute;left:569px;top:504px;width:142px;height:277px;background:var(--navy);overflow:hidden;color:#fff}
.wheel-label{position:absolute;font-size:4.2px;line-height:1.3}

/* Tiles */
.tiles-label{position:absolute;left:766px;top:601px;font-size:10.5px;font-weight:600;color:var(--teal)}
.tiles-label span{font-weight:400}
.tile{position:absolute;top:622px;height:169px;overflow:hidden;color:#fff}
.tile .icon-dot{width:36px;height:36px;position:absolute;left:12px;top:12px}
.tile h5{position:absolute;left:13px;top:54px;font-size:11px;font-weight:700;line-height:1.2;text-transform:uppercase}
.tile p{position:absolute;left:13px;font-size:7.2px;line-height:1.45}
</style>
</head>
<body>

<svg width="0" height="0" style="position:absolute" aria-hidden="true">
  <symbol id="i-people" viewBox="0 0 24 24"><circle cx="12" cy="6" r="2.3"/><circle cx="5.5" cy="8" r="1.9"/><circle cx="18.5" cy="8" r="1.9"/><path d="M8.5 19v-5a3.5 3.5 0 0 1 7 0v5M2.5 18v-3.5a3 3 0 0 1 5-2.2M21.5 18v-3.5a3 3 0 0 0-5-2.2"/></symbol>
  <symbol id="i-network" viewBox="0 0 24 24"><circle cx="12" cy="12" r="2.4"/><circle cx="12" cy="3.5" r="1.6"/><circle cx="12" cy="20.5" r="1.6"/><circle cx="4.5" cy="8" r="1.6"/><circle cx="19.5" cy="8" r="1.6"/><circle cx="4.5" cy="16" r="1.6"/><circle cx="19.5" cy="16" r="1.6"/><path d="M12 5v4.6M12 14.4V19M6 8.8l4 2M18 8.8l-4 2M6 15.2l4-2M18 15.2l-4-2"/></symbol>
  <symbol id="i-chat" viewBox="0 0 24 24"><path d="M3 10a6 5 0 0 1 12 0a6 5 0 0 1-8 4.7L4 16l.9-2.8A5 5 0 0 1 3 10z"/><path d="M16.5 8.5A5 4.5 0 0 1 20 17l.8 2.6-2.9-1.2A5.5 4.5 0 0 1 10 17"/></symbol>
  <symbol id="i-sprout" viewBox="0 0 24 24"><path d="M12 20v-8M12 12c0-4 3-6 7-6c0 4-3 6-7 6zM12 14c0-3-2.5-5-6-5c0 3 2.5 5 6 5z"/><path d="M4 20h16"/></symbol>
  <symbol id="i-hand" viewBox="0 0 24 24"><path d="M3 16l4-2h5l3 1.5-3 1H9M3 19l4-1 7 .5 6-4.5"/><path d="M13 11V6M13 7c0-2 2-3.5 4-3.5 0 2-2 3.5-4 3.5zM13 8.5c0-1.8-1.6-3-3.5-3 0 1.8 1.6 3 3.5 3z"/></symbol>
</svg>

<!-- BROCHURE OUTSIDE: COVER -->
<section class="panel cover">
  <div class="abs" role="img" aria-label="Eucalyptus leaf sprig decoration" style="right:0;top:20px;width:60px;height:80px;background:radial-gradient(ellipse at 60% 40%,#7ba33a 0%,rgba(123,163,58,0) 70%)"></div>
  <p class="abs eyebrow" style="left:29px;top:49px">Shared Guidelines for</p>
  <h1 class="abs" style="left:28px;top:64px"><span class="title-a" style="display:block;font-size:40px">Community</span><span class="title-b" style="display:block;font-size:42px;margin-top:2px">Renewal</span></h1>
  <p class="abs" style="left:29px;top:162px;width:200px;font-size:12px;line-height:1.45">Working together to help communities <span class="hl">recover</span> and <span class="hl">thrive</span>.</p>
  <div class="abs" role="img" aria-label="Illustration of families holding hands across rolling green hills with a gum tree" style="left:0;top:200px;width:261px;height:215px;background:linear-gradient(180deg,rgba(15,42,58,0) 0%,#6f8f45 35%,#c9c98a 60%,#3f6a36 80%,#1f4a2e 100%)"></div>
  <div class="abs brand" style="left:29px;top:432px;color:#fff">
    <span class="mark" style="width:36px;height:36px"></span>
    <span><span class="name" style="display:block;font-size:10px">Community Renewal<br>Network</span><span class="sub" style="display:block;font-size:7px;margin-top:2px">AUSTRALIA</span></span>
  </div>
</section>

<!-- BROCHURE OUTSIDE: PARTNERS -->
<section class="panel partners">
  <p class="abs" style="left:0;right:0;top:29px;text-align:center;font-size:8.5px;font-weight:500;letter-spacing:.3px">PARTNERS IN DEVELOPMENT FROM THE</p>
  <div class="partner-grid">
    <div class="partner"><span class="shape"></span>Federal Office of Community Affairs</div>
    <div class="partner"><span class="shape"></span>Federal Office of Social Support</div>
    <div class="partner"><span class="shape"></span>Harbour Aid Society</div>
    <div class="partner"><span class="shape"></span>Southern State Council</div>
    <div class="partner"><span class="shape"></span>Western State Council</div>
    <div class="partner"><span class="shape"></span>Island State Council</div>
    <div class="partner"><span class="shape"></span>Northern Coast Council</div>
    <div class="partner"><span class="shape"></span>Capital Region Council</div>
    <div class="partner"><span class="shape"></span>Top End Region Council</div>
    <div class="partner"><span class="shape"></span>Southeast State Council</div>
    <div class="partner"><span class="shape"></span>Eastern State Office of Community Readiness</div>
  </div>
  <div class="abs brand" style="left:25px;top:432px;color:var(--teal)">
    <span class="mark" style="width:40px;height:40px"></span>
    <span style="color:var(--navy)"><span class="name" style="display:block;font-size:9px">Community Renewal<br>Network</span><span class="sub" style="display:block;font-size:6.5px;margin-top:1px">AUSTRALIA</span></span>
  </div>
  <p class="abs" style="left:72px;top:474px;font-size:8.5px;color:var(--teal)">renewalnetwork.org.au</p>
</section>

<!-- BROCHURE OUTSIDE: ABOUT -->
<section class="panel about">
  <h2 class="abs h-teal" style="left:16px;top:26px">About the principles</h2>
  <span class="abs icon-dot" style="left:14px;top:50px;width:50px;height:50px;background:var(--lime)"><svg><use href="#i-people"/></svg></span>
  <p class="abs body-s" style="left:73px;top:53px;width:172px">Disaster recovery is part of emergency management, which includes the broader components of prevention, preparedness and response. Planning for recovery is integral to emergency preparation, and mitigation actions are often initiated as part of recovery.</p>
  <span class="abs icon-dot" style="left:14px;top:140px;width:50px;height:50px;background:var(--teal)"><svg><use href="#i-hand"/></svg></span>
  <p class="abs body-s" style="left:73px;top:143px;width:172px">Disaster recovery includes built, environmental and economic elements, all contributing to individual and social wellbeing. Recovery can provide an opportunity to improve these aspects beyond previous conditions, contributing to a more resilient community.</p>
  <h2 class="abs h-teal" style="left:16px;top:244px;line-height:1.2">The relationship between<br>the principles</h2>
  <p class="abs body-s" style="left:16px;top:276px;width:160px">While all the principles are equally critical to ensure effective recovery, understanding the local and broader context and recognising complexity are foundational.</p>
  <p class="abs body-s" style="left:16px;top:325px;width:160px">The descriptions beneath each principle overleaf provide further guidance for working with communities in disaster recovery.</p>
  <div class="abs" role="img" aria-label="Illustration of a diverse community walking together past homes and trees at sunrise" style="left:0;top:365px;width:252px;height:137px;background:linear-gradient(180deg,rgba(244,240,226,0) 0%,#d9d6a8 30%,#7ba33a 62%,#2f5a3a 100%)"></div>
</section>

<!-- POSTER -->
<section class="poster">
  <div class="poster-top"></div>
  <div class="abs" role="img" aria-label="Eucalyptus leaf branch decoration" style="right:0;top:0;width:110px;height:115px;background:radial-gradient(ellipse at 60% 45%,#8ab63e 0%,rgba(123,163,58,0) 70%)"></div>
  <p class="abs eyebrow" style="left:27px;top:30px;color:#fff">Shared Guidelines for</p>
  <h2 class="abs" style="left:26px;top:42px"><span class="title-a" style="display:block;font-size:38px">Community</span><span class="title-b" style="display:block;font-size:38px">Renewal</span></h2>
  <span class="abs pill" style="left:27px;top:128px">SUCCESSFUL RECOVERY</span>

  <div class="principle" style="top:157px"><span class="icon-dot" style="background:var(--lime)"><svg><use href="#i-people"/></svg></span><div><h3>Understand the <b>CONTEXT</b></h3><p>Successful recovery is based on an understanding of the community context, with each community having its own history, values and dynamics.</p></div></div>
  <div class="principle" style="top:211px"><span class="icon-dot" style="background:var(--teal)"><svg><use href="#i-network"/></svg></span><div><h3>Recognise <b>COMPLEXITY</b></h3><p>Successful recovery is responsive to the complex and evolving nature of disasters and their impacts on communities.</p></div></div>
  <div class="principle" style="top:265px"><span class="icon-dot" style="background:var(--lime)"><svg><use href="#i-people"/></svg></span><div><h3>Use <b>COMMUNITY-LED</b> approaches</h3><p>Successful recovery is community-centred, responsive and flexible, engaging with community and supporting them to move forward.</p></div></div>
  <div class="principle" style="top:319px"><span class="icon-dot" style="background:var(--teal)"><svg><use href="#i-network"/></svg></span><div><h3><b>COORDINATE</b> all activities</h3><p>Successful recovery requires a planned, coordinated and adaptive approach between community and partner agencies, based on continuing assessment of impacts and needs.</p></div></div>
  <div class="principle" style="top:373px"><span class="icon-dot" style="background:var(--blue)"><svg><use href="#i-chat"/></svg></span><div><h3><b>COMMUNICATE</b> effectively</h3><p>Successful recovery is built on effective communication between the affected community and other partners.</p></div></div>
  <div class="principle" style="top:427px"><span class="icon-dot" style="background:var(--lime)"><svg><use href="#i-sprout"/></svg></span><div><h3>Recognise and build <b>CAPACITY</b></h3><p>Successful recovery recognises, supports and builds on individual, community and organisational capacity and resilience.</p></div></div>

  <div class="abs" role="img" aria-label="Illustration of families and a house among gum trees on green hills" style="left:0;top:478px;width:373px;height:101px;background:linear-gradient(180deg,rgba(244,240,226,0) 0%,#9fb866 30%,#2f5a3a 65%,#0f2a3a 100%)"></div>
  <div class="abs brand" style="left:26px;top:540px;color:#fff">
    <span class="mark" style="width:32px;height:32px"></span>
    <span><span class="name" style="display:block;font-size:8px">Community Renewal<br>Network</span><span class="sub" style="display:block;font-size:5.5px;margin-top:1px">AUSTRALIA</span></span>
  </div>
  <p class="abs" style="right:22px;top:558px;font-size:9px;font-weight:500;color:#fff">renewalnetwork.org.au</p>
</section>

<!-- 3C FOUNDATION -->
<section class="threec">
  <h2 class="abs" style="left:22px;top:14px;font-size:10px;font-weight:600;color:var(--navy)">THE 3C FOUNDATION OF RECOVERY</h2>
  <svg class="abs" style="left:0;top:0" width="300" height="268" aria-hidden="true">
    <circle cx="144" cy="150" r="112" fill="none" stroke="#c5cca0" stroke-width="2"/>
    <circle cx="144" cy="150" r="100" fill="#dfe3c4"/>
    <circle cx="152" cy="74" r="50" fill="#cfd6a8"/>
    <circle cx="226" cy="165" r="46" fill="#c9d39c"/>
    <circle cx="72" cy="172" r="56" fill="#2f7a7a"/>
    <circle cx="144" cy="135" r="41" fill="var(--forest)" stroke="#fff" stroke-width="3"/>
    <circle cx="226" cy="140" r="24" fill="var(--lime)"/>
    <circle cx="72" cy="140" r="20" fill="#4a9a98"/>
    <path d="M92 96 L86 108 M86 108 l-3 -4 M86 108 l4 -2" stroke="#4b5652" fill="none" stroke-width="1.2"/>
    <path d="M262 150 C280 150 285 120 295 95 M262 150 C282 150 290 140 295 130 M262 155 C282 165 285 185 295 188" stroke="#7ba33a" fill="none" stroke-width="1" stroke-dasharray="3 3"/>
  </svg>
  <svg class="abs" style="left:118px;top:40px;width:20px;height:20px;stroke:#4b5652;fill:none;stroke-width:1.5" aria-hidden="true"><use href="#i-people"/></svg>
  <p class="abs c-label" style="left:142px;top:44px;font-weight:500;font-size:9px;color:var(--ink)">CONTEXT</p>
  <p class="abs c-text" style="left:142px;top:57px;width:58px">Understanding the community, its history, values and dynamics.</p>
  <p class="abs" style="left:104px;top:116px;width:80px;text-align:center;font-size:9.5px;font-weight:500;color:#fff">RECOVERY</p>
  <p class="abs c-text" style="left:112px;top:130px;width:64px;text-align:center;color:#fff">Stronger, more resilient communities together.</p>
  <svg class="abs" style="left:61px;top:129px;width:22px;height:22px;stroke:#fff;fill:none;stroke-width:1.5" aria-hidden="true"><use href="#i-network"/></svg>
  <svg class="abs" style="left:214px;top:128px;width:24px;height:24px;stroke:#fff;fill:none;stroke-width:1.5" aria-hidden="true"><use href="#i-people"/></svg>
  <p class="abs c-label" style="left:32px;top:166px;width:80px;text-align:center;color:#fff">COMPLEXITY</p>
  <p class="abs c-text" style="left:36px;top:178px;width:72px;text-align:center;color:#fff">Recognising the complex, evolving nature of disasters.</p>
  <p class="abs c-label" style="left:186px;top:170px;width:80px;text-align:center;color:var(--navy)">COMMUNITY-LED</p>
  <p class="abs c-text" style="left:194px;top:182px;width:64px;text-align:center">Putting community at the centre of recovery.</p>

  <p class="abs" style="left:306px;top:28px;font-size:7.8px;font-weight:600;color:var(--navy)">BUILT ON BY THREE ENABLING PRINCIPLES</p>
  <div class="enabler" style="top:53px"><span class="icon-dot" style="background:var(--teal)"><svg><use href="#i-network"/></svg></span><div><h4>COORDINATE</h4><p>Working together in a planned, adaptive and inclusive way.</p></div></div>
  <div class="enabler" style="top:116px"><span class="icon-dot" style="background:var(--blue)"><svg><use href="#i-chat"/></svg></span><div><h4>COMMUNICATE</h4><p>Sharing the right information, clearly and consistently.</p></div></div>
  <div class="enabler" style="top:178px"><span class="icon-dot" style="background:var(--lime)"><svg><use href="#i-sprout"/></svg></span><div><h4>CAPACITY</h4><p>Building the skills, resilience and resources we need.</p></div></div>
</section>

<!-- PULL-UP BANNER -->
<section class="banner">
  <p class="abs" style="left:16px;top:28px;font-size:5px;font-weight:600;letter-spacing:.2px">SHARED GUIDELINES FOR</p>
  <h2 class="abs" style="left:15px;top:35px"><span class="title-a" style="display:block;font-size:19px">Community</span><span class="title-b" style="display:block;font-size:19px">Renewal</span></h2>
  <p class="abs" style="left:16px;top:78px;width:110px;font-size:6px;line-height:1.4">Working together to help communities <span class="hl">recover</span> and <span class="hl">thrive</span>.</p>
  <svg class="abs" style="left:30px;top:122px" width="82" height="82" viewBox="-41 -41 82 82" aria-hidden="true">
    <circle r="40" fill="#fff"/>
    <path d="M0 0 L0 -37 A37 37 0 0 1 32 -18.5 Z" fill="var(--lime)"/>
    <path d="M0 0 L32 -18.5 A37 37 0 0 1 32 18.5 Z" fill="var(--teal)"/>
    <path d="M0 0 L32 18.5 A37 37 0 0 1 0 37 Z" fill="var(--lime)"/>
    <path d="M0 0 L0 37 A37 37 0 0 1 -32 18.5 Z" fill="var(--teal)"/>
    <path d="M0 0 L-32 18.5 A37 37 0 0 1 -32 -18.5 Z" fill="var(--blue)"/>
    <path d="M0 0 L-32 -18.5 A37 37 0 0 1 0 -37 Z" fill="var(--forest)"/>
    <circle r="14" fill="#fff"/>
    <g stroke="#fff" stroke-width="1" fill="none"><line x1="0" y1="0" x2="0" y2="-37"/><line x1="0" y1="0" x2="32" y2="-18.5"/><line x1="0" y1="0" x2="32" y2="18.5"/><line x1="0" y1="0" x2="0" y2="37"/><line x1="0" y1="0" x2="-32" y2="18.5"/><line x1="0" y1="0" x2="-32" y2="-18.5"/></g>
  </svg>
  <p class="wheel-label" style="left:48px;top:106px;width:46px;text-align:center">Understand the CONTEXT</p>
  <p class="wheel-label" style="left:110px;top:129px;width:30px">Recognise COMPLEXITY</p>
  <p class="wheel-label" style="left:4px;top:129px;width:28px">Recognise and build CAPACITY</p>
  <p class="wheel-label" style="left:3px;top:184px;width:30px">COMMUNICATE effectively</p>
  <p class="wheel-label" style="left:110px;top:184px;width:30px">Use COMMUNITY-LED approaches</p>
  <p class="wheel-label" style="left:48px;top:208px;width:46px;text-align:center">COORDINATE all activities</p>
  <div class="abs" role="img" aria-label="Illustration of a community walking together on green hills" style="left:0;top:220px;width:142px;height:36px;background:linear-gradient(180deg,rgba(15,42,58,0) 0%,#6f8f45 55%,#1f4a2e 100%)"></div>
  <div class="abs brand" style="left:10px;top:259px;color:#fff;gap:4px">
    <span class="mark" style="width:12px;height:12px;border-width:1px"></span>
    <span class="name" style="font-size:4.3px">Community Renewal<br>Network</span>
  </div>
  <p class="abs" style="right:8px;top:263px;font-size:5px">renewalnetwork.org.au</p>
</section>

<!-- SOCIAL TILES -->
<p class="tiles-label">SOCIAL MEDIA TILES <span>(3 EXAMPLES)</span></p>

<article class="tile" style="left:758px;width:131px;background:var(--navy)">
  <span class="icon-dot" style="background:var(--lime)"><svg><use href="#i-hand"/></svg></span>
  <h5>Communities<br>recover<br><span style="color:var(--lime-soft)">together</span></h5>
  <p style="top:104px">People. Connection.<br>Hope. Resilience.</p>
  <div class="abs" role="img" aria-label="Illustration of families among trees on rolling hills" style="left:0;top:128px;width:131px;height:41px;background:linear-gradient(180deg,rgba(15,42,58,0) 0%,#7ba33a 55%,#2f5a3a 100%)"></div>
</article>

<article class="tile" style="left:895px;width:143px;background:var(--teal)">
  <span class="icon-dot" style="background:#2a8088;border:1.5px solid #fff"><svg><use href="#i-network"/></svg></span>
  <h5>Recovery is<br>collaborative</h5>
  <p style="top:90px;width:115px">Many sectors, one goal – stronger communities.</p>
  <div class="abs" role="img" aria-label="Illustration of a diverse group joining hands in a circle" style="left:0;top:120px;width:143px;height:49px;background:linear-gradient(180deg,rgba(29,106,112,0) 0%,#c98b5a 45%,#3c5a4a 100%)"></div>
</article>

<article class="tile" style="left:1044px;width:144px;background:var(--lime)">
  <span class="icon-dot" style="background:#9bbc52"><svg><use href="#i-sprout"/></svg></span>
  <h5>Building<br>capacity for<br>tomorrow</h5>
  <p style="top:104px;width:100px">Strengthening people, organisations and communities.</p>
  <div class="abs" role="img" aria-label="Growing sprout and curved hills decoration" style="left:0;top:136px;width:144px;height:33px;background:linear-gradient(180deg,rgba(123,163,58,0) 0%,#c7c255 55%,#5d8a2e 100%)"></div>
</article>

</body>
</html>
```